Veltrane New Business Card Design IT Company

PLEASE CHECK ATTACHED PDF DOC FOR DETAILS. I have put exactly what I want to save time and finish the project asap thanks.

Veltrane Consulting is an Information Management Consulting company providing IT Professional Services Consulting services to both Public and private sector.
Need a Business Card Design to represent. It has to be Premium Raised Spot Glass finish.
Company Name: Veltrane Consulting
Company Website: veltrane-example.com.au
Company Slogan: High Performance Meets Excellence
Name on Card: Lor Bemis
Title: Managing Partner
Email: Lor.Bemis@veltrane-example.com.au
Phone: 0400000000

Company Logo is under construction from SketchHive
Company Logo & Company Name Font Color should Match and have to Electric Aqua Blue
Company Logo at the Back Side of the Card
Card Background color preference: Slight Grey or Black to make the logo and company Name stand Out.

Any Questions please Ask.

Industry/Entity Type

Construction

Contact Information for Business Card

PLEASE CHECK ATTACHED PDF DOC FOR DETAILS. I have put exactly what I want to save time and finish the project asap thanks
Name on Card: Lor Bemis
Title: Managing Partner
Phone: 0400000000

Requirements
Must have
• PLEASE CHECK ATTACHED PDF DOC FOR DETAILS. I have put exactly what I want to save time and finish the project asap thanks
• Company Logo, Company Name, Company website Company Slogan at the back side of the Card with custom dark blue front and back background
• Company Logo, Company Name , Company Website at the Front of the Card Title and Name email and phone in the front also in white color font
Should not have
• Should not Have Decorative or Script Fonts
• Its a IT company so must be professional no flowers or waterfalls etc

```html
<!DOCTYPE html>
<html lang="en">
<head>
<meta charset="utf-8">
<title>Veltrane Consulting – Business Card</title>
<link rel="stylesheet" href="https://fonts.googleapis.com/css2?family=Questrial&family=Poppins:wght@600&display=swap">
<style>
  :root {
    --page: #ffffff;
    --card-dark: #0a0d10;
    --card-dark-mark: #15191d;
    --card-light: #a7abb2;
    --card-light-mark: #b2b6bc;
    --aqua: #3ec6ee;
    --aqua-deep: #1f7fd0;
    --slogan: #2fd8ee;
    --white: #ffffff;
  }
  * { margin: 0; padding: 0; box-sizing: border-box; }
  html, body {
    width: 916px;
    height: 1200px;
    overflow: hidden;
    background: var(--page);
  }
  body {
    position: relative;
    font-family: "Questrial", "Century Gothic", sans-serif;
  }
  .card {
    position: absolute;
    left: 48px;
    width: 822px;
    height: 508px;
    overflow: hidden;
  }
  .card--back { top: 68px; background: var(--card-dark); }
  .card--front { top: 625px; background: var(--card-light); }

  .card__watermark {
    position: absolute;
    left: 150px;
    top: 30px;
    width: 520px;
    height: 520px;
    border-radius: 50%;
    border: 70px solid var(--card-dark-mark);
  }
  .card--front .card__watermark { border-color: var(--card-light-mark); top: 20px; }

  .brand-dot {
    position: absolute;
    border-radius: 50%;
    background: linear-gradient(180deg, var(--aqua-deep), var(--aqua));
  }
  .card--back .brand-dot { left: 351px; top: 122px; width: 120px; height: 120px; }

  .brand-name {
    position: absolute;
    left: 0;
    width: 100%;
    text-align: center;
    color: var(--aqua);
  }
  .card--back .brand-name { top: 272px; font-size: 54px; line-height: 64px; letter-spacing: 0.5px; }

  .slogan {
    position: absolute;
    top: 352px;
    left: 0;
    width: 100%;
    text-align: center;
    font-size: 23px;
    line-height: 28px;
    letter-spacing: 0.3px;
    color: var(--slogan);
  }
  .website {
    position: absolute;
    top: 458px;
    left: 0;
    width: 100%;
    text-align: center;
    font-size: 25px;
    line-height: 30px;
    color: var(--white);
  }

  .front-brand {
    position: absolute;
    right: 40px;
    top: 48px;
    display: flex;
    align-items: center;
    gap: 12px;
  }
  .front-brand .brand-dot { position: static; width: 80px; height: 80px; }
  .front-brand__name { font-size: 30px; color: var(--aqua-deep); }

  .person {
    position: absolute;
    top: 228px;
    left: 0;
    width: 100%;
    text-align: center;
    color: var(--white);
  }
  .person__name {
    font-family: "Poppins", "Century Gothic", sans-serif;
    font-weight: 600;
    font-size: 42px;
    line-height: 50px;
  }
  .person__title { font-size: 23px; line-height: 28px; margin-top: 2px; }

  .contact {
    position: absolute;
    left: 52px;
    top: 378px;
    list-style: none;
    font-size: 24px;
    line-height: 31px;
    color: var(--white);
  }
</style>
</head>
<body>
  <section class="card card--back" aria-label="Card back">
    <div class="card__watermark" aria-hidden="true"></div>
    <div class="brand-dot" aria-hidden="true"></div>
    <p class="brand-name">Veltrane Consulting</p>
    <p class="slogan">high performance meets excellence</p>
    <p class="website">veltrane-example.com.au</p>
  </section>

  <section class="card card--front" aria-label="Card front">
    <div class="card__watermark" aria-hidden="true"></div>
    <div class="front-brand">
      <span class="brand-dot" aria-hidden="true"></span>
      <span class="front-brand__name">Veltrane</span>
    </div>
    <div class="person">
      <h1 class="person__name">Lor Bemis</h1>
      <p class="person__title">Managing Partner</p>
    </div>
    <ul class="contact">
      <li>Phone: 040 000 0000</li>
      <li>Email: Lor.Bemis@veltrane-example.com.au</li>
      <li>Web: veltrane-example.com.au</li>
    </ul>
  </section>
</body>
</html>
```